life insurance quote website design for levoletclairdor.ca

the web site levoletclairdor.ca need a design. we dont like the actuel one but we are open at all new suggestion. visit us at levoletclairdor.ca and you will understand. the principal concurant is tarifcouvertureplume.ca, datoroves.ca, coutbouclierfixe.ca. We are a life insurance quote site. we found best price available in the canadien industrie. We absolutly want a design with our form in the front page on the top right side like our concurance, we use wordpress at this time. we want to be able to switch language. and to have a logic form. we want to be able to change the color for each type of insurance quote page.we also need a blog in it to post news. and the site will be SEO accurate.

Target Market(s)

Get client fill the quote form

Industry/Entity Type

Insurance

Number of Pages Required

3 page

Font styles to use
Sans Serif

Requirements
Must have
• logic form on the top right first page
• page template for product info stuff, contact, and who we are, blog
• French site
• custum color
Nice to have
• Wordpress design will be appréciate
• switch language english/french

```html
<!DOCTYPE html>
<html lang="en">
<head>
<meta charset="utf-8">
<title>Le Volet Clair d'Or — Life Insurance Quotes</title>
<link rel="stylesheet" href="https://fonts.googleapis.com/css2?family=Open+Sans:wght@300;400;600;700&family=Source+Sans+3:wght@300;400;600;700&display=swap">
<style>
:root{
  --red:#b3111a;
  --red-dark:#7a0a10;
  --red-deep:#6a0b10;
  --blue:#1566b3;
  --blue-deep:#0c4f99;
  --ink:#333;
  --muted:#666;
  --line:#c9c9c9;
  --gold:#f2c21a;
  --white:#fff;
  --footer-text:#f3e6e6;
}
*{box-sizing:border-box;margin:0;padding:0}
html,body{width:1200px;height:2639px;overflow:hidden}
body{position:relative;background:var(--white);font-family:"Source Sans 3",Arial,sans-serif;color:var(--ink)}
.abs{position:absolute}

/* header */
.brand{left:176px;top:68px;display:flex;align-items:center;gap:12px}
.brand-mark{width:34px;height:34px;background:var(--red)}
.brand-name{font-size:30px;font-weight:700;color:var(--red);line-height:1.1;white-space:nowrap}
.lang{left:829px;top:51px;width:121px;height:26px;border:1px solid var(--line);border-radius:4px;font-size:13px;color:#999;display:flex;align-items:center;justify-content:space-between;padding:0 8px;letter-spacing:.5px}
.lang i{width:24px;height:14px;background:linear-gradient(#c33 0 33%,#fff 33% 66%,#1c3f8f 66%)}
.contact-line{left:744px;display:flex;align-items:center;gap:14px;color:#222}
.contact-line.phone{top:90px;font-size:24px;font-weight:600}
.contact-line.mail{top:124px;font-size:18px}

/* nav */
.nav{left:0;top:195px;width:1200px;height:65px;background:linear-gradient(#c8141d,#8d0a10);display:flex;align-items:stretch;padding-left:180px}
.nav a{color:var(--white);text-decoration:none;font-size:19px;padding:0 17px;display:flex;align-items:center;border-right:1px solid rgba(0,0,0,.25)}
.nav a.active{background:linear-gradient(#2a86d6,#135fa8)}
.nav a:last-of-type{border-right:0}
.search{position:absolute;left:857px;top:18px;width:188px;height:28px;background:var(--white);border-radius:14px;font-size:14px;font-style:italic;color:#aaa;display:flex;align-items:center;justify-content:space-between;padding:0 12px}

/* hero */
.hero{left:0;top:260px;width:1200px;height:453px;background:
  radial-gradient(ellipse 420px 300px at 520px 260px,#d9a07a 0,#b07a56 40%,rgba(120,90,60,0) 100%),
  linear-gradient(90deg,#4c5a2c,#6f7a3e 45%,#3f5a26)}
.hero-tag{left:174px;top:405px;color:var(--white);font-size:28px;font-weight:300;line-height:40px;letter-spacing:.5px}
.dots{display:flex;gap:6px}
.dots span{width:13px;height:13px;border-radius:50%;border:2px solid var(--white)}
.dots span.on{background:var(--white)}

/* quote form */
.quote{left:797px;top:326px;width:349px;height:396px;background:var(--white);border-radius:8px;box-shadow:0 6px 12px rgba(0,0,0,.35);overflow:hidden}
.quote h2{height:53px;background:linear-gradient(#c8141d,#8d0a10);color:var(--white);text-align:center;font:700 26px/53px "Source Sans 3",sans-serif}
.quote .row{position:absolute;left:20px;right:12px;display:flex;align-items:center;font-size:13px;color:var(--red-dark)}
.quote .row label{width:70px;text-align:right;padding-right:8px}
.field{height:22px;border:1px solid var(--line);background:var(--white);flex:1}
.select{position:relative}
.select::after{content:"";position:absolute;right:6px;top:8px;border:5px solid transparent;border-top-color:#777}
.quote .type{font-size:10px;font-style:italic;color:#888;padding:4px 6px}
.check{width:14px;height:14px;border:1px solid #999;margin-right:8px}
.submit{position:absolute;left:75px;top:328px;width:225px;height:48px;border-radius:24px;background:linear-gradient(#ffe45a,#e8b40c);border:2px solid #c99700;color:#4a2a00;font:700 24px/44px "Source Sans 3",sans-serif;text-align:center;letter-spacing:1px}

/* welcome */
.section-title{font-family:"Open Sans",sans-serif;text-align:center;width:1200px;left:0}
.welcome-title{top:745px;font-size:29px;color:#444}
.welcome-title b{font-weight:400;color:var(--red)}
.welcome-title em{font-style:normal;color:var(--blue)}
.underline{left:560px;width:80px;border-top:2px dotted #aaa}
.welcome-text{left:180px;top:802px;width:844px;font-size:12.4px;line-height:16px;text-align:justify;color:#444}
.btn-red{left:517px;top:903px;width:191px;height:46px;background:linear-gradient(#c8141d,#8d0a10);border-radius:5px;color:var(--white);text-align:center;font-size:18px;line-height:46px}

/* products band */
.band{left:0;top:980px;width:1200px;height:389px;background:linear-gradient(120deg,#8e0d13,#b0141c 50%,#7d0b10)}
.band-title{top:1020px;color:var(--white);font-weight:700;font-size:28px;letter-spacing:.5px}
.card{top:1110px;width:224px;height:200px;border:1px solid rgba(255,255,255,.8);color:var(--white);text-align:center}
.card .icon{position:absolute;left:75px;top:-38px;width:74px;height:74px;border-radius:50%;background:var(--red);border:2px solid var(--white);display:flex;align-items:center;justify-content:center}
.card h3{margin-top:44px;font-size:18px;font-weight:600}
.card p{font-size:11px;line-height:14px;padding:0 10px;text-align:left;margin-top:4px}
.card .more{position:absolute;left:46px;bottom:-10px;width:132px;height:22px;border:1px solid var(--white);border-radius:11px;background:var(--red-dark);font-size:11px;line-height:20px}

/* blog */
.blog-title{top:1395px;font-size:29px;color:#444}
.blog-sub{top:1460px;font-size:12px;color:#666}
.post{top:1503px;width:271px}
.post .photo{height:176px}
.post .date{margin-top:14px;font-size:11px;color:#555;display:flex;align-items:center;gap:8px}
.post .date i{width:14px;height:13px;border:2px solid #555;border-top-width:4px}
.post h4{margin-top:8px;font-size:11.5px;color:var(--red);font-weight:600}
.post p{font-size:11px;color:#666;line-height:14px;margin-top:2px}
.post p span{color:var(--blue);font-weight:700}

/* testimonials */
.testi{left:0;top:1802px;width:1200px;height:312px;background:linear-gradient(115deg,#0e5fb0,#1a70c0 50%,#0b4f99)}
.testi-title{top:1822px;color:var(--white);font-size:29px}
.avatar{left:569px;top:1887px;width:62px;height:62px;border-radius:50%;border:3px solid var(--white);background:radial-gradient(circle,#d7a47c,#8a5a3a)}
.testi-name{top:1956px;color:var(--white);font-size:19px}
.testi-quote{left:205px;top:1994px;width:790px;text-align:center;color:var(--white);font-size:19px;line-height:24px}

/* newsletter */
.help{left:178px;top:2204px;color:#222}
.help small{display:block;font-size:13px}
.help strong{display:block;font-size:19px;font-weight:600}
.help strong span{font-weight:400}
.help big{display:block;font-size:38px;color:var(--red-dark);font-weight:300;line-height:44px;margin-top:6px}
.mail-circle{left:449px;top:2203px;width:100px;height:100px;border-radius:50%;border:3px solid var(--blue-deep);display:flex;align-items:center;justify-content:center}
.news-title{left:572px;top:2158px;font-size:38px;font-weight:300;color:var(--blue)}
.news-sub{left:574px;top:2204px;font-size:18px;color:#999}
.news-input{left:572px;top:2240px;width:283px;height:46px;border:1px solid var(--line)}
.news-btn{left:862px;top:2238px;width:166px;height:50px;background:linear-gradient(#2a86d6,#135fa8);color:var(--white);font-size:23px;text-align:center;line-height:50px;box-shadow:0 3px 4px rgba(0,0,0,.3)}

/* footer */
.footer{left:0;top:2371px;width:1200px;height:229px;background:var(--red-deep)}
.fcol{top:2388px;font-size:11px;line-height:17px;color:var(--footer-text)}
.fcol h5{font-size:15px;font-weight:600;color:var(--white);border-bottom:1px dotted rgba(255,255,255,.6);padding-bottom:4px;margin-bottom:10px}
.fcol b{font-weight:700;color:var(--white)}
.social{display:flex;gap:6px}
.social i{width:36px;height:36px;border-radius:50%;background:#c9a9a9}
.badge{width:152px;height:78px;background:var(--white);margin-top:18px}
.copyright{left:0;top:2600px;width:1200px;height:39px;background:var(--blue-deep);color:var(--white);font-size:11px;text-align:center;line-height:39px}
</style>
</head>
<body>

<header>
  <div class="abs brand"><span class="brand-mark"></span><span class="brand-name">Le Volet Clair d'Or</span></div>
  <div class="abs lang">ENGLISH <i role="img" aria-label="Language flag"></i></div>
  <div class="abs contact-line phone">
    <svg width="26" height="24" viewBox="0 0 24 24"><path fill="#b3111a" d="M6.6 10.8a15 15 0 0 0 6.6 6.6l2.2-2.2c.3-.3.7-.4 1-.2 1.1.4 2.3.6 3.6.6.6 0 1 .4 1 1V20c0 .6-.4 1-1 1A17 17 0 0 1 3 4c0-.6.4-1 1-1h3.5c.6 0 1 .4 1 1 0 1.3.2 2.5.6 3.6.1.3 0 .7-.2 1z"/></svg>
    1-855-412-7730
  </div>
  <div class="abs contact-line mail">
    <svg width="26" height="18" viewBox="0 0 26 18"><rect width="26" height="18" fill="#b3111a"/><path d="M1 1l12 9 12-9" stroke="#fff" stroke-width="2" fill="none"/></svg>
    contact@levoletclairdor.ca
  </div>
</header>

<nav class="abs nav">
  <a class="active">Home</a><a>Who Are We?</a><a>Products</a><a>Submission</a><a>Blog</a><a>Contact Us</a>
  <div class="search">Search...
    <svg width="14" height="14" viewBox="0 0 14 14"><circle cx="6" cy="6" r="4.5" stroke="#222" stroke-width="2" fill="none"/><path d="M9.5 9.5L13 13" stroke="#222" stroke-width="2.4"/></svg>
  </div>
</nav>

<section>
  <div class="abs hero" role="img" aria-label="Photo: smiling family of four outdoors in a sunny park"></div>
  <p class="abs hero-tag">SERVICE RAPIDE<br>GRATUIT ET<br>CONFINDENTIAL</p>
  <div class="abs dots" style="left:567px;top:677px"><span class="on"></span><span></span><span></span><span></span></div>

  <form class="abs quote">
    <h2>Request A Quote</h2>
    <div class="row" style="top:69px"><div class="field select type">Type of Insurance</div></div>
    <div class="row" style="top:105px"><label>Name:</label><div class="field"></div></div>
    <div class="row" style="top:142px"><label>Email:</label><div class="field"></div></div>
    <div class="row" style="top:179px"><label>Phone:</label><div class="field" style="flex:0 0 52px"></div><div class="field" style="flex:0 0 52px;margin-left:10px"></div><div class="field" style="margin-left:10px"></div></div>
    <div class="row" style="top:216px"><label>Location:</label><div class="field select"></div></div>
    <div class="row" style="top:250px"><label>Age:</label><div class="field select" style="flex:0 0 68px"></div><label style="width:78px">Gender:</label><div class="field select"></div></div>
    <div class="row" style="top:290px;font-size:10px;color:#666"><span class="check"></span>I have read and accept the use and privacy policy of *</div>
    <div class="submit">SUBMIT</div>
  </form>
</section>

<section>
  <h2 class="abs section-title welcome-title" style="font-weight:400">Welcome to <b>Le</b> <em>Volet Clair d'Or</em></h2>
  <div class="abs underline" style="top:790px"></div>
  <p class="abs welcome-text">Lorem ipsum dolor sits amet consectetur adipiscing elit. Quid sequatur quid repugnet vident. Duo Reges constructio interrete. Tollitur beneficium tollitur gratia quae sunt vincla concordiae. Age, inquies, ista parva sunt. Hoc ipsum elegantius poni meliusque potuit. Aufert enim sensus actionemque tollit omnem. Ut nemo dubitet eorum omnia officia quo spectare quid sequi quid fugere debeant Summae mihi videtur inscitiae. Expectoque quid ad id quod quaerebam respondeas.</p>
  <a class="abs btn-red">Read more</a>
</section>

<section>
  <div class="abs band"></div>
  <h2 class="abs section-title band-title">FIND THE BEST INSURANCE AT THE BEST PRICE!</h2>

  <article class="abs card" style="left:132px">
    <div class="icon"><svg width="40" height="40" viewBox="0 0 40 40" fill="none" stroke="#fff" stroke-width="2"><path d="M4 20a16 14 0 0 1 32 0z"/><path d="M20 20v12a3 3 0 0 1-6 0"/></svg></div>
    <h3>Life Insurance</h3>
    <p>Un service rapide, gratuit et confidentiel.<br><br>Remplissez le formulaire de soumission assurance vie et vous apprécierez votre expérience avec nous</p>
    <div class="more">Read more...</div>
  </article>
  <article class="abs card" style="left:370px">
    <div class="icon"><svg width="40" height="40" viewBox="0 0 40 40" fill="none" stroke="#fff" stroke-width="2"><circle cx="20" cy="15" r="10"/><path d="M23 11h-4a2 2 0 0 0 0 4h2a2 2 0 0 1 0 4h-4M20 8v14"/><path d="M4 30h10l6 4h14"/></svg></div>
    <h3>Salary Insurance</h3>
    <p>Un service rapide, gratuit et confidentiel.<br><br>Remplissez le formulaire de soumission assurance salaire et vous apprécierez votre expérience avec nous.</p>
    <div class="more">Read more...</div>
  </article>
  <article class="abs card" style="left:609px">
    <div class="icon"><svg width="40" height="40" viewBox="0 0 40 40" fill="none" stroke="#fff" stroke-width="2"><path d="M6 20L20 8l14 12M10 17v14h20V17"/><path d="M17 31v-8h6v8"/></svg></div>
    <h3>Mortgage Insurance</h3>
    <p>Un service rapide, gratuit et confidentiel<br><br>Remplissez le formulaire de soumission assurance hypothécaire et vous apprécierez votre expérience avec nous,</p>
    <div class="more">Read more...</div>
  </article>
  <article class="abs card" style="left:845px">
    <div class="icon"><svg width="40" height="40" viewBox="0 0 40 40" fill="none" stroke="#fff" stroke-width="2"><rect x="11" y="7" width="18" height="26"/><path d="M15 14h10M15 19h10M15 24h6M18 29h4"/></svg></div>
    <h3>Critical Illness Insurance</h3>
    <p>Un service rapide, gratuit et confidentiel.<br><br>Remplissez le formulaire de soumission assurance maladies grave et vous apprécierez votre expérience avec nous,</p>
    <div class="more">Read more...</div>
  </article>
</section>

<section>
  <h2 class="abs section-title blog-title" style="font-weight:400">Blog News</h2>
  <div class="abs underline" style="top:1441px"></div>
  <p class="abs section-title blog-sub">Uas iracundia his ea errem ridens nam an veniam equidem. Lorem ipsum dolor sit amet lore ipsum dolor sit amet</p>

  <article class="abs post" style="left:180px">
    <div class="photo" role="img" aria-label="Photo: hands reviewing financial charts on an office desk" style="background:linear-gradient(135deg,#f2f4f6 0,#d3dbe1 50%,#8fa3b0 100%)"></div>
    <div class="date"><i></i>Febuary 11, 2016</div>
    <h4>Aufert enim sensus actionemque tollit omnem.</h4>
    <p>Donec laoreet non nec aliquam pellentesque interdum <span>→</span></p>
  </article>
  <article class="abs post" style="left:465px">
    <div class="photo" role="img" aria-label="Photo: mother and child playing outdoors in warm sunlight" style="background:linear-gradient(135deg,#f0c66a 0,#d6984a 50%,#7f5a26 100%)"></div>
    <div class="date"><i></i>Febuary 11, 2016</div>
    <h4>Aufert enim sensus actionemque tollit omnem.</h4>
    <p>Donec laoreet non nec aliquam pellentesque interdum <span>→</span></p>
  </article>
  <article class="abs post" style="left:748px">
    <div class="photo" role="img" aria-label="Photo: senior couple smiling together in an autumn park" style="background:linear-gradient(135deg,#5f7a3a 0,#9a7b4a 50%,#b0402e 100%)"></div>
    <div class="date"><i></i>Febuary 11, 2016</div>
    <h4>Aufert enim sensus actionemque tollit omnem.</h4>
    <p>Donec laoreet non nec aliquam pellentesque interdum <span>→</span></p>
  </article>
</section>

<section>
  <div class="abs testi" role="img" aria-label="Background photo: person writing, tinted blue"></div>
  <h2 class="abs section-title testi-title" style="font-weight:400">Testimonials</h2>
  <div class="abs underline" style="top:1866px;left:555px;width:90px;border-color:rgba(255,255,255,.7)"></div>
  <div class="abs avatar" role="img" aria-label="Client portrait photo"></div>
  <p class="abs section-title testi-name">Jane Doe</p>
  <p class="abs testi-quote">Lorem ipsum dolor sit amet, consectetur adipisicing elit. Quibusdam quod explicabo optio quia ex odit, sequi harum voluptatibus autem. Nam autem corporis deleniti fugiat omnis itaque, quis laudantium dolor facere.</p>
  <div class="abs dots" style="left:578px;top:2085px"><span class="on" style="width:11px;height:11px;border:0"></span><span style="width:11px;height:11px;border:0;background:rgba(255,255,255,.5)"></span><span style="width:11px;height:11px;border:0;background:rgba(255,255,255,.5)"></span></div>
</section>

<section>
  <div class="abs help"><small>NEED HELP IN</small><strong>CHOOSING BEST <span>FOR YOU?</span></strong><big>MAIL US</big></div>
  <div class="abs mail-circle"><svg width="50" height="34" viewBox="0 0 50 34"><rect width="50" height="34" fill="#0c4f99"/><path d="M2 2l23 17L48 2" stroke="#fff" stroke-width="3" fill="none"/></svg></div>
  <h2 class="abs news-title">NEWSLETTER</h2>
  <p class="abs news-sub">We will keep you update with latest news</p>
  <div class="abs news-input"></div>
  <div class="abs news-btn">Subscribe</div>
</section>

<footer>
  <div class="abs footer"></div>
  <div class="abs fcol" style="left:178px;width:130px">
    <h5>Navigation</h5>
    Home<br>Who Are We?<br>Products<br>Submission<br>Blog<br>Contact Us
  </div>
  <div class="abs fcol" style="left:347px;width:240px">
    <h5>Our Offices</h5>
    <b>The head office</b><br>48 Rue des Tilleuls, La Prairie, QC, J5R 0A1<br><b>Towns</b><br>Montreal, Quebec, Sherbrooke, Granby Beauce, three Rivières, Piedmont, Saguenay Goods, Chicoutimi, Sept-îles, Rouyn-Noranda Val D'Or, Gatineau, Victoriaville, Amqui, Wolf River Chateauguay, La Prairie
  </div>
  <div class="abs fcol" style="left:635px;width:220px">
    <h5>Hours of Operation</h5>
    Our hours of operation<br><br><b>Monday to Friday:</b> 7am to 21hrs<br><b>Sunday:</b> 10hrs to 15hrs<br><b>Toll free:</b> 1-855-412-7730<br><b>Email:</b> contact@levoletclairdor.ca
  </div>
  <div class="abs fcol" style="left:883px;width:170px">
    <h5 style="border:0">Follow Us</h5>
    <div class="social"><i role="img" aria-label="Social link"></i><i role="img" aria-label="Social link"></i><i role="img" aria-label="Social link"></i><i role="img" aria-label="Social link"></i></div>
    <div class="badge" role="img" aria-label="Professional membership badge"></div>
  </div>
  <div class="abs copyright">Copyright © 2016. Le Volet Clair d'Or.</div>
</footer>

</body>
</html>
```